Billboard Design for Equipment Rental Business

We need a billboard design for our equipment rental business called Brindlewood Equipment Company. We are based in Georgia. We rent construction tools, equipment, and dumpsters. We currently have a design but feel like we could get something better. Our phone number is 912-730-2591 and our website is www.brindlewoodequipment-example.com

```html
<!DOCTYPE html>
<html lang="en">
<head>
<meta charset="UTF-8">
<title>Brindlewood Equipment Company — Billboard</title>
<link rel="stylesheet" href="https://fonts.googleapis.com/css2?family=Krona+One&family=Oswald:wght@700&display=swap">
<style>
  :root {
    --yellow: #f7b916;
    --black: #111111;
    --white: #ffffff;
    --stage: #7a7a7a;
    --sky: #e8f1f8;
    --dirt: #8a6a3e;
    --steel: #4a5360;
  }
  html, body {
    margin: 0;
    width: 1200px;
    height: 1112px;
    overflow: hidden;
    background: var(--stage);
  }
  .billboard {
    position: absolute;
    left: 30px;
    top: 348px;
    width: 1890px;
    height: 690px;
    transform: scale(0.6032);
    transform-origin: 0 0;
    overflow: hidden;
    background: var(--yellow);
  }
  .billboard__shapes {
    position: absolute;
    inset: 0;
  }
  .brand {
    position: absolute;
    left: 70px;
    top: 30px;
    font-family: "Oswald", sans-serif;
    font-weight: 700;
    color: var(--black);
    line-height: 1;
  }
  .brand__name {
    display: block;
    font-size: 132px;
    letter-spacing: 0.01em;
  }
  .brand__sub {
    display: block;
    margin-top: 14px;
    font-size: 50px;
    letter-spacing: 0.12em;
  }
  .offer__title {
    position: absolute;
    left: 100px;
    top: 266px;
    margin: 0;
    font-family: "Krona One", sans-serif;
    font-size: 72px;
    line-height: 1;
    color: var(--yellow);
    letter-spacing: -0.02em;
  }
  .offer__list {
    position: absolute;
    left: 0;
    top: 368px;
    margin: 0;
    padding: 0;
    list-style: none;
    font-family: "Krona One", sans-serif;
    font-size: 58px;
    line-height: 70px;
    color: var(--black);
    letter-spacing: -0.03em;
  }
  .offer__item {
    position: relative;
    padding-left: 48px;
  }
  .offer__item::before {
    content: "";
    position: absolute;
    left: 0;
    top: 17px;
    width: 32px;
    height: 38px;
    background: var(--black);
    clip-path: polygon(0 0, 65% 0, 100% 50%, 65% 100%, 0 100%, 25% 50%);
  }
  .contact {
    position: absolute;
    display: flex;
    align-items: center;
    gap: 14px;
    font-family: "Krona One", sans-serif;
    line-height: 1;
  }
  .contact--phone {
    left: 44px;
    top: 600px;
    height: 76px;
    font-size: 66px;
    color: var(--white);
    letter-spacing: -0.03em;
  }
  .contact--web {
    left: 958px;
    top: 600px;
    height: 76px;
    font-size: 29px;
    color: var(--black);
    letter-spacing: -0.01em;
  }
  .contact__icon {
    flex: none;
  }
</style>
</head>
<body>
  <section class="billboard" aria-label="Brindlewood Equipment Company billboard">
    <svg class="billboard__shapes" viewBox="0 0 1890 690" width="1890" height="690" aria-hidden="false">
      <defs>
        <linearGradient id="photoTone" x1="0" y1="0" x2="1" y2="1">
          <stop offset="0" stop-color="var(--sky)"/>
          <stop offset="0.45" stop-color="#b59a74"/>
          <stop offset="0.7" stop-color="var(--steel)"/>
          <stop offset="1" stop-color="#d9c7a4"/>
        </linearGradient>
      </defs>
      <polygon class="hero-photo" role="img" aria-label="Photo of an excavator bucket lifting a load of dirt against a bright sky"
               points="985,0 1890,0 1890,585 1360,585" fill="url(#photoTone)"/>
      <polygon class="divider-stripe" points="885,0 985,0 1315,585 1265,585" fill="var(--black)"/>
      <polygon class="offer-banner" points="0,258 680,258 735,355 0,355" fill="var(--black)"/>
      <polygon class="footer-phone" points="0,585 870,585 945,690 0,690" fill="var(--black)"/>
      <polygon class="footer-accent" points="870,585 892,585 967,690 945,690" fill="var(--yellow)"/>
      <polygon class="footer-web" points="892,585 1890,585 1890,690 967,690" fill="var(--white)"/>
    </svg>

    <div class="brand">
      <span class="brand__name">BRINDLEWOOD</span>
      <span class="brand__sub">EQUIPMENT COMPANY</span>
    </div>

    <h2 class="offer__title">WE RENT</h2>
    <ul class="offer__list">
      <li class="offer__item">CONSTRUCTION TOOLS</li>
      <li class="offer__item">EQUIPMENT AND</li>
      <li class="offer__item">DUMPSTERS</li>
    </ul>

    <div class="contact contact--phone">
      <svg class="contact__icon" width="42" height="42" viewBox="0 0 24 24" aria-hidden="true">
        <path d="M6.6 10.8c1.4 2.8 3.8 5.1 6.6 6.6l2.2-2.2c.3-.3.7-.4 1-.2 1.1.4 2.3.6 3.6.6.6 0 1 .4 1 1V20c0 .6-.4 1-1 1C10.6 21 3 13.4 3 4c0-.6.4-1 1-1h3.5c.6 0 1 .4 1 1 0 1.3.2 2.5.6 3.6.1.3 0 .7-.2 1l-2.3 2.2z" fill="var(--yellow)"/>
      </svg>
      <span class="contact__text">912-730-2591</span>
    </div>

    <div class="contact contact--web">
      <svg class="contact__icon" width="40" height="40" viewBox="0 0 24 24" aria-hidden="true">
        <g fill="none" stroke="var(--yellow)" stroke-width="1.6">
          <circle cx="12" cy="12" r="10"/>
          <ellipse cx="12" cy="12" rx="4.5" ry="10"/>
          <line x1="2" y1="12" x2="22" y2="12"/>
          <path d="M4 7h16M4 17h16"/>
        </g>
      </svg>
      <span class="contact__text">BRINDLEWOODEQUIPMENT-EXAMPLE.COM</span>
    </div>
  </section>
</body>
</html>
```